Fernvale Craft Works business card design- Fine Art sculpture business (Contract guaranteed)

This business card is for a fine art business. Though we don't have a website up and running yet it should be up soon. I would like the business card to be elegant and fairly simple with a picture of one of my sculptures on the front (you might need to photoshop out the background) as well as my basic contact info (my name,phone # and e-mail). On the back I'd like it to be pretty simple with just "Notes" and some blank lines for writing in info.

Target Market(s)

High end artwork buyers

Industry/Entity Type

Art Gallery

Contact Information for Business Card

Marlo Prewitt Phone: (555) 213-4098 E-mail: marlo@quillbrookmail.com Facebook: @fernvalecraftworks Instagram: fernvalecraftworks

Colors

Designer to choose colors to be used in the design.

Requirements
Must have
• *A picture of one of my sculptures*, my name, business name (Fernvale Craft Works), e-mail, phone #, and a notes section on the back.
• Fernvale Craft Works
• Marlo Prewitt
• (555)213-4098
• marlo@quillbrookmail.com
• Facebook: @fernvalecraftworks
• Instagram: fernvalecraftworks
Nice to have
• It'd be nice if you can crop out the background in the sculpture pictures, which ever one you end up using.

```html
<!DOCTYPE html>
<html lang="en">
<head>
<meta charset="utf-8">
<title>Fernvale Craft Works — Business Card</title>
<link rel="stylesheet" href="https://fonts.googleapis.com/css2?family=Cinzel:wght@500;600&family=Montserrat:wght@400&display=swap">
<style>
  :root {
    --page: #ffffff;
    --card: #ffffff;
    --ink: #111111;
    --accent: #1f5a2a;
    --rule: #3a3a3a;
    --stone-dark: #14321f;
    --stone-mid: #1f7a3d;
    --stone-light: #3da35f;
  }
  html, body {
    margin: 0;
    padding: 0;
    width: 1200px;
    height: 1200px;
    overflow: hidden;
    background: var(--page);
  }
  .canvas {
    position: relative;
    width: 1200px;
    height: 1200px;
  }
  .card {
    position: absolute;
    width: 631px;
    height: 359px;
    background: var(--card);
    border-radius: 14px;
    box-shadow: 0 1px 6px rgba(0,0,0,0.28);
    overflow: hidden;
  }
  .card--front { left: 84px; top: 264px; }
  .card--back  { left: 487px; top: 581px; }

  .accent-rule {
    position: absolute;
    height: 3px;
    background: var(--accent);
  }
  .wordmark {
    position: absolute;
    margin: 0;
    font-family: "Cinzel", serif;
    font-weight: 600;
    font-size: 24px;
    line-height: 26px;
    letter-spacing: 0.5px;
    color: var(--ink);
    text-align: right;
    white-space: nowrap;
  }
  .wordmark span { display: block; }

  /* Front */
  .card--front .accent-rule { left: 0; top: 46px; width: 268px; }
  .card--front .wordmark { right: 363px; top: 58px; }
  .contact {
    position: absolute;
    left: 44px;
    top: 168px;
  }
  .contact__name {
    margin: 0 0 4px;
    font-family: "Cinzel", serif;
    font-weight: 500;
    font-size: 26px;
    letter-spacing: 0.5px;
    color: var(--ink);
  }
  .contact__line {
    margin: 0;
    font-family: "Montserrat", sans-serif;
    font-size: 18px;
    line-height: 26px;
    color: var(--ink);
  }
  .contact__line--social {
    font-size: 14px;
    line-height: 21px;
  }
  .contact__social { margin-top: 4px; }
  .sculpture {
    position: absolute;
    left: 462px;
    top: 36px;
    width: 108px;
    height: 280px;
    border-radius: 40px 24px 20px 20px;
    background: linear-gradient(160deg, var(--stone-light) 0%, var(--stone-mid) 45%, var(--stone-dark) 100%);
  }

  /* Back */
  .card--back .accent-rule--top { left: 0; top: 63px; width: 125px; }
  .notes__title {
    position: absolute;
    left: 45px;
    top: 76px;
    margin: 0;
    font-family: "Cinzel", serif;
    font-weight: 600;
    font-size: 20px;
    letter-spacing: 1px;
    color: var(--ink);
  }
  .notes__lines {
    position: absolute;
    left: 45px;
    top: 143px;
  }
  .card--back .wordmark { right: 55px; top: 150px; }
  .card--back .accent-rule--bottom { right: 0; top: 207px; width: 106px; }
</style>
</head>
<body>
<main class="canvas">

  <section class="card card--front" aria-label="Business card front">
    <div class="accent-rule"></div>
    <p class="wordmark"><span>Fernvale</span><span>Craft Works</span></p>
    <div class="contact">
      <p class="contact__name">MARLO PREWITT</p>
      <p class="contact__line">(555) 213-4098</p>
      <p class="contact__line">marlo@quillbrookmail.com</p>
      <div class="contact__social">
        <p class="contact__line contact__line--social">Facebook: @fernvalecraftworks</p>
        <p class="contact__line contact__line--social">Instagram: fernvalecraftworks</p>
      </div>
    </div>
    <div class="sculpture" role="img" aria-label="Photograph of a green malachite stone sculpture on a round base"></div>
  </section>

  <section class="card card--back" aria-label="Business card back">
    <div class="accent-rule accent-rule--top"></div>
    <p class="notes__title">NOTES</p>
    <svg class="notes__lines" width="293" height="124" viewBox="0 0 293 124" aria-hidden="true">
      <g stroke="var(--rule)" stroke-width="2">
        <line x1="0" y1="1" x2="293" y2="1"/>
        <line x1="0" y1="31" x2="293" y2="31"/>
        <line x1="0" y1="61" x2="293" y2="61"/>
        <line x1="0" y1="91" x2="293" y2="91"/>
        <line x1="0" y1="121" x2="293" y2="121"/>
      </g>
    </svg>
    <p class="wordmark"><span>Fernvale</span><span>Craft Works</span></p>
    <div class="accent-rule accent-rule--bottom"></div>
  </section>

</main>
</body>
</html>
```